KLOMB Systems website

We need a website design using much of the information on the KLOMB flyer (attached) we just had a PixelBarn designer create. We'd like a WordPress Site, no need for a shopping cart attached to it. It should have an About us page, Book titles page, a blog page, Membership and Navigators pages contact us and privacy policy and terms of services.

```html
<!DOCTYPE html>
<html lang="en">
<head>
<meta charset="utf-8">
<title>KLOMB Systems</title>
<link href="https://fonts.googleapis.com/css2?family=Montserrat:wght@400;600;700&family=Open+Sans:wght@300;400;600;700&display=swap" rel="stylesheet">
<style>
:root{
  --brand:#4a7bbb;
  --brand-dark:#2d5b97;
  --navy:#1f3f6e;
  --ink:#3c3c3c;
  --muted:#7a7a7a;
  --soft:#f4f5f7;
  --line:#e3e5e8;
  --footer:#2a2b2d;
  --footer-deep:#202123;
  --teal:#46a68f;
  --red:#ee5a2c;
  --orange:#f6941e;
  --sky:#2aa3dc;
  --green:#3aab49;
  --white:#ffffff;
}
*{margin:0;padding:0;box-sizing:border-box}
html,body{width:1200px;height:3422px;overflow:hidden}
body{font-family:"Open Sans",Arial,sans-serif;color:var(--ink);background:var(--white);position:relative}
.abs{position:absolute}
h2.section-title{position:absolute;left:0;width:1200px;text-align:center;font-family:"Montserrat",Arial,sans-serif;font-weight:700;font-size:30px;color:#4a4a4a;letter-spacing:.5px}
.title-rule{position:absolute;left:575px;width:50px;height:3px;background:var(--brand)}

/* top bar */
.topbar{top:0;left:0;width:1200px;height:32px;background:var(--brand-dark);color:var(--white);font-size:11px}
.topbar .consult{left:160px;top:9px;font-weight:600}
.topbar .account{right:162px;top:9px;letter-spacing:.5px}

/* header */
.site-header{top:32px;left:0;width:1200px;height:123px;background:var(--white)}
.logo{display:flex;align-items:center;gap:10px;font-family:"Montserrat",Arial,sans-serif;font-weight:700;color:var(--brand-dark)}
.site-header .logo{left:160px;top:40px;font-size:38px}
.logo .dot{width:30px;height:30px;border-radius:50%;background:var(--brand)}
.main-nav{left:433px;top:58px;display:flex;gap:36px;font-family:"Montserrat",Arial,sans-serif;font-size:11.5px;font-weight:600;color:#3a3a3a}
.main-nav .active{color:var(--brand)}

/* hero */
.hero{top:155px;left:0;width:1200px;height:511px;background:linear-gradient(180deg,#5d7ea8 0%,#3e5f8c 45%,#2c4466 100%)}
.hero .city{position:absolute;inset:0;background:linear-gradient(90deg,rgba(20,35,60,.55),rgba(80,110,150,.2) 50%,rgba(20,35,60,.55))}
.hero .hero-mark{left:0;width:1200px;top:98px;text-align:center;font-family:"Montserrat",Arial,sans-serif;font-weight:700;font-size:30px;color:var(--white);letter-spacing:2px}
.hero h1{left:0;width:1200px;top:220px;text-align:center;font-family:"Montserrat",Arial,sans-serif;font-weight:700;font-size:42px;color:var(--white);letter-spacing:.5px}
.hero h1 sup{font-size:14px;vertical-align:super}
.hero .subline{left:0;width:1200px;top:272px;text-align:center;font-family:"Montserrat",Arial,sans-serif;font-weight:400;font-size:38px;color:var(--white)}
.hero .btn-ghost{left:525px;top:347px;width:150px;height:41px;border:2px solid var(--white);border-radius:21px;color:var(--white);font-size:12px;font-weight:600;letter-spacing:1px;display:flex;align-items:center;justify-content:center}
.hero .arrow{top:250px;color:var(--white);font-size:22px}
.hero .dots{left:578px;top:465px;display:flex;gap:6px}
.hero .dots span{width:11px;height:11px;border-radius:50%;border:1.5px solid var(--white)}
.hero .dots span.on{background:var(--white)}

/* services */
.services{top:666px;left:0;width:1200px;height:783px;background:var(--soft)}
.info-box{background:var(--white);box-shadow:0 2px 8px rgba(0,0,0,.06);padding:16px 20px;font-size:10.5px;line-height:1.45;color:#555}
.info-box li{list-style:none;position:relative;padding-left:16px;margin-bottom:6px}
.info-box li::before{content:"";position:absolute;left:0;top:4px;width:7px;height:7px;border-radius:50%;background:#666}
.diagram{left:0;top:0}
.node-label{position:absolute;text-align:center;color:var(--white);font-family:"Montserrat",Arial,sans-serif;font-weight:700;font-size:13px;line-height:1.3;width:130px}

/* formula */
.formula{top:1449px;left:0;width:1200px;height:463px;background:var(--white)}
.pillar{top:132px;width:166px;height:271px;color:var(--white);text-align:center;padding-top:20px}
.pillar .icon{width:52px;height:52px;margin:0 auto}
.pillar h3{font-family:"Montserrat",Arial,sans-serif;font-size:13px;font-weight:700;margin-top:14px;letter-spacing:.3px}
.pillar .lead{font-size:8.5px;font-weight:600;line-height:1.35;margin:12px 8px 12px;text-transform:uppercase;white-space:nowrap}
.pillar ul{text-align:left;margin-left:16px;font-size:10px;font-weight:600}
.pillar li{list-style:none;margin-bottom:9px;display:flex;align-items:center;gap:7px;white-space:nowrap}
.pillar li::before{content:"";width:11px;height:11px;border-radius:50%;border:2px solid var(--white);flex:none}

/* testimonials */
.testimonials{top:1912px;left:0;width:1200px;height:449px;background:var(--soft)}
.quote-card{top:150px;height:196px;background:var(--white);padding:26px 28px}
.quote-card p{font-size:12.5px;line-height:1.6;color:#555}
.quote-card .who{position:absolute;left:28px;top:132px;display:flex;align-items:center;gap:12px;font-size:11px;font-weight:700;color:#444}
.quote-card .who::before{content:"";width:26px;height:1px;background:#999}
.quote-card .role{position:absolute;left:66px;top:152px;font-size:10px;color:var(--muted)}
.quote-card .qmark{position:absolute;right:26px;top:118px;font-family:Georgia,serif;font-size:84px;line-height:1;color:#e4e6ea}
.pager{top:380px;width:22px;height:22px;border-radius:50%;border:1px solid #bbb;color:#999;font-size:12px;display:flex;align-items:center;justify-content:center}

/* news */
.news{top:2361px;left:0;width:1200px;height:518px;background:var(--white)}
.news-card{top:157px;width:280px;height:288px;background:var(--soft)}
.news-card .photo{width:280px;height:176px}
.news-card .date{position:absolute;left:14px;top:0;width:48px;height:44px;background:var(--brand);color:var(--white);text-align:center;font-family:"Montserrat",Arial,sans-serif;font-weight:700;font-size:16px;line-height:1.1;padding-top:6px}
.news-card .date small{display:block;font-size:9px}
.news-card h4{margin:20px 22px 8px;font-family:"Montserrat",Arial,sans-serif;font-size:13px;font-weight:700;color:var(--brand);line-height:1.35}
.meta{font-size:10px;color:#999}
.news-card .meta{margin-left:22px}
.news-item{left:760px;width:278px;height:66px;display:flex;gap:14px}
.news-item .thumb{width:88px;height:56px;flex:none}
.news-item h5{font-family:"Montserrat",Arial,sans-serif;font-size:10.5px;font-weight:700;color:var(--brand);line-height:1.3;margin-bottom:6px}

/* cta */
.cta{top:2879px;left:0;width:1200px;height:118px;background:var(--brand-dark)}
.cta h3{left:160px;top:40px;font-family:"Montserrat",Arial,sans-serif;font-size:22px;font-weight:700;color:var(--white)}
.cta .btn{left:901px;top:41px;width:137px;height:41px;background:var(--white);color:var(--brand-dark);font-size:12px;font-weight:700;letter-spacing:.5px;display:flex;align-items:center;justify-content:center}

/* footer */
.site-footer{top:2997px;left:0;width:1200px;height:311px;background:var(--footer);color:#d8d8d8}
.contact-row{left:160px;top:30px;display:flex;align-items:center;gap:14px;font-size:11.5px;font-weight:600;color:var(--white)}
.contact-row .ic{width:22px;height:22px;border:1px solid #777;border-radius:3px;display:flex;align-items:center;justify-content:center}
.site-footer .logo{right:162px;top:18px;font-size:36px;color:var(--white)}
.site-footer .logo .dot{background:var(--white);width:26px;height:26px}
.footer-rule{left:160px;top:80px;width:878px;height:1px;background:#444}
.about-col{left:160px;top:106px;width:265px}
.about-col h4{font-size:11px;font-weight:700;color:var(--white);margin-bottom:14px}
.about-col p{font-size:10px;line-height:1.75;color:#cfcfcf}
.link-col{top:106px;font-size:10px;line-height:2.1;color:#cfcfcf}
.link-col li{list-style:none;padding-left:12px;position:relative}
.link-col li::before{content:"›";position:absolute;left:0}
.signup{left:776px;top:106px;width:262px}
.signup label{font-size:10.5px;color:var(--white);display:block;margin-bottom:10px}
.signup .field{height:30px;background:var(--white);color:#999;font-size:10px;padding:8px 10px}
.signup .btn{margin-top:16px;width:82px;height:32px;background:var(--brand);color:var(--white);font-size:10.5px;font-weight:700;display:flex;align-items:center;justify-content:center}
.bottom-bar{top:3308px;left:0;width:1200px;height:114px;background:var(--footer-deep)}
.social{left:557px;top:20px;display:flex;gap:12px}
.social span{width:20px;height:20px;border-radius:50%;background:var(--brand)}
.copyright{left:0;width:1200px;top:70px;text-align:center;font-size:10px;color:#aaa}
</style>
</head>
<body>

<div class="abs topbar">
  <div class="abs consult">For Free Consultation: 555-010-2722</div>
  <div class="abs account">REGISTER &nbsp;|&nbsp; SIGN IN</div>
</div>

<header class="abs site-header">
  <div class="abs logo"><span class="dot"></span>KLOMB</div>
  <nav class="abs main-nav">
    <span class="active">HOME</span><span>ABOUT US</span><span>BOOK TITLES</span><span>BLOG</span><span>MEMBERSHIP</span><span>NAVIGATORS</span><span>CONTACT US</span>
  </nav>
</header>

<section class="abs hero" role="img" aria-label="Business handshake in front of a city skyline at dusk">
  <div class="city"></div>
  <div class="abs hero-mark">KLOMB</div>
  <h1 class="abs">BECOME A KLOMB<sup>™</sup> MEMEBER TODAY</h1>
  <div class="abs subline">AND YOU WILL RECEIVE...</div>
  <div class="abs btn-ghost">LEARN MORE</div>
  <div class="abs arrow" style="left:24px">‹</div>
  <div class="abs arrow" style="right:24px">›</div>
  <div class="abs dots"><span class="on"></span><span></span><span></span></div>
</section>

<section class="abs services">
  <h2 class="section-title" style="top:62px">SERVICE WE OFFER</h2>
  <div class="title-rule" style="top:112px"></div>

  <ul class="abs info-box" style="left:668px;top:151px;width:329px">
    <li>KLOMB™ Strategy Stack - for clarity and alignment</li>
    <li>Collection of simple, streamlined tools and processes</li>
    <li>A structured system that ensures productivity and accountability</li>
    <li>"It's a journey, not an event"</li>
  </ul>
  <ul class="abs info-box" style="left:851px;top:365px;width:267px">
    <li>Guided by your personal Navigator</li>
    <li>Builds your leadership team through structured learning, communication and teambuilding initiatives</li>
    <li>Monthly one-on-one coaching for the business leader</li>
    <li>Monthly connection with leadership team</li>
  </ul>
  <ul class="abs info-box" style="left:791px;top:570px;width:327px">
    <li>Pre-developed business processes</li>
    <li>Simplified business templates and forms</li>
    <li>Reference materials</li>
    <li>Business Book Summaries</li>
  </ul>
  <ul class="abs info-box" style="left:80px;top:570px;width:340px">
    <li>Easy, online, automated system</li>
    <li>Dashboards and tracking tools</li>
    <li>Shared accessibility and accountability</li>
    <li>Private Online Storage Area</li>
  </ul>
  <ul class="abs info-box" style="left:18px;top:365px;width:324px">
    <li>Online, self-paced learning modules, 20 to 30 minutes each</li>
    <li>Leadership Development topics – Communications, Management, Decision-Making</li>
    <li>Employee Development topics – Time Management, Goal Achievement, Self-Development</li>
    <li>Includes Learning Content, Quizzes, Study Guides, Discussion Questions, Development Path</li>
  </ul>

  <svg class="abs diagram" width="1200" height="783" viewBox="0 0 1200 783">
    <circle cx="607" cy="444" r="175" fill="none" stroke="#c9d3e2" stroke-width="14"/>
    <g fill="none" stroke="#dfe5ee" stroke-width="2">
      <polyline points="607,269 710,586 441,390 773,390 504,586 607,269"/>
    </g>
    <circle cx="607" cy="444" r="92" fill="var(--brand)" stroke="#d3dcea" stroke-width="6"/>
    <g fill="var(--brand)" stroke="#d3dcea" stroke-width="5">
      <circle cx="607" cy="269" r="72"/>
      <circle cx="773" cy="390" r="72"/>
      <circle cx="710" cy="586" r="72"/>
      <circle cx="504" cy="586" r="72"/>
      <circle cx="441" cy="390" r="72"/>
    </g>
    <text x="607" y="456" text-anchor="middle" fill="#fff" font-family="Montserrat, Arial, sans-serif" font-weight="700" font-size="34">KLOMB</text>
  </svg>
  <div class="node-label" style="left:542px;top:248px">KLOMB™<br>Business<br>Methodology</div>
  <div class="node-label" style="left:708px;top:369px">KLOMB™<br>Leadership<br>Development</div>
  <div class="node-label" style="left:645px;top:573px">KLOMB™<br>Library</div>
  <div class="node-label" style="left:439px;top:565px">KLOMB™<br>Technology<br>Platform</div>
  <div class="node-label" style="left:376px;top:369px">KLOMB™<br>Learning<br>Center</div>
</section>

<section class="abs formula">
  <h2 class="section-title" style="top:56px;font-size:22px">KLOMB™ = STRATEGY, TEAM, ACTION, ACCOUNTABILITY, RESULTS</h2>
  <div class="title-rule" style="top:95px"></div>

  <div class="abs pillar" style="left:160px;background:var(--teal)">
    <svg class="icon" viewBox="0 0 52 52" fill="none" stroke="#fff" stroke-width="2.5"><circle cx="24" cy="28" r="18"/><circle cx="24" cy="28" r="10"/><circle cx="24" cy="28" r="3" fill="#fff"/><path d="M24 28 L44 8 M38 8h6v6"/></svg>
    <h3>STRATEGY</h3>
    <div class="lead">Long term vision,<br>tactical planning</div>
    <ul><li>Strategy Stack</li><li>Marketing Plan</li><li>Financial Plan</li><li>Operating Plan</li></ul>
  </div>
  <div class="abs pillar" style="left:338px;background:var(--red)">
    <svg class="icon" viewBox="0 0 52 52" fill="#fff"><circle cx="26" cy="16" r="7"/><circle cx="12" cy="20" r="5"/><circle cx="40" cy="20" r="5"/><path d="M14 42c0-9 5-15 12-15s12 6 12 15z"/><path d="M3 40c0-7 4-11 9-11 2 0 3 .5 4 1-3 3-4 6-4 10z"/><path d="M49 40c0-7-4-11-9-11-2 0-3 .5-4 1 3 3 4 6 4 10z"/></svg>
    <h3>TEAM</h3>
    <div class="lead">Healthy team relationships<br>&amp; development</div>
    <ul><li>Right People, Right Seats</li><li>Team Health</li><li>Learning &amp; Development</li></ul>
  </div>
  <div class="abs pillar" style="left:516px;background:var(--orange)">
    <svg class="icon" viewBox="0 0 52 52" fill="none" stroke="#fff" stroke-width="2.5" stroke-linejoin="round"><path d="M20 30V10a4 4 0 0 1 8 0v14l10 2c3 1 5 3 4 7l-2 10c-1 3-3 5-6 5H24c-3 0-5-2-7-4l-7-9c-1-2 0-4 2-4 2 0 4 2 8 6"/><path d="M14 12a10 10 0 0 1 20 0"/></svg>
    <h3>ACTION</h3>
    <div class="lead">Processes to execute the<br>vision</div>
    <ul><li>Operating processes</li><li>Action plans</li></ul>
  </div>
  <div class="abs pillar" style="left:694px;background:var(--sky)">
    <svg class="icon" viewBox="0 0 52 52" fill="none" stroke="#fff" stroke-width="3"><circle cx="22" cy="22" r="14"/><path d="M32 32l14 14" stroke-width="5" stroke-linecap="round"/></svg>
    <h3>ACCOUNTABILITY</h3>
    <div class="lead">Tools and checklists<br>to stay on track</div>
    <ul><li>Online Tracking Tools</li><li>Targets, Tasks and Topics</li></ul>
  </div>
  <div class="abs pillar" style="left:872px;background:var(--green)">
    <svg class="icon" viewBox="0 0 52 52" fill="none" stroke="#fff" stroke-width="2.5"><circle cx="24" cy="24" r="16"/><path d="M36 36l10 10" stroke-width="4" stroke-linecap="round"/><path d="M17 30v-6M24 30V16M31 30v-10"/></svg>
    <h3>RESULTS</h3>
    <div class="lead">Dashboards – company &amp;<br>department</div>
    <ul><li>Dashboards</li><li>Weekly KPIs</li></ul>
  </div>
</section>

<section class="abs testimonials">
  <h2 class="section-title" style="top:56px;font-size:22px">TESTIMONIALS</h2>
  <div class="title-rule" style="top:95px"></div>
  <div class="abs quote-card" style="left:160px;width:438px">
    <p>Lorem ipsum dolor sit amet, consectetur adipiscing elit. Quisque et lectus vitae massa ornare pharetra sit amet non lacus. Aliquam condimentum eros ante, vitae tempus odio molestie a.</p>
    <div class="who">John Doe</div>
    <div class="role">Co-Founder of Company</div>
    <div class="qmark">”</div>
  </div>
  <div class="abs quote-card" style="left:611px;width:427px">
    <p>Lorem ipsum dolor sit amet, consectetur adipiscing elit. Quisque et lectus vitae massa ornare pharetra sit amet non lacus. Aliquam condimentum eros ante, vitae tempus odio molestie a.</p>
    <div class="who">John Doe</div>
    <div class="role">Co-Founder of Company</div>
    <div class="qmark">”</div>
  </div>
  <div class="abs pager" style="left:571px">‹</div>
  <div class="abs pager" style="left:603px">›</div>
</section>

<section class="abs news">
  <h2 class="section-title" style="top:62px;font-size:22px">LATEST NEWS</h2>
  <div class="title-rule" style="top:100px"></div>

  <article class="abs news-card" style="left:160px">
    <div class="photo" role="img" aria-label="Team hands reviewing printed charts on a desk" style="background:linear-gradient(135deg,#c9ccd1,#7b838e)"></div>
    <div class="date">04<small>OCT</small></div>
    <h4>BUSINESS GROWTH DEPENDS<br>ON YOUR MARKETING</h4>
    <div class="meta">admin &nbsp;/&nbsp; 0 Comments</div>
  </article>
  <article class="abs news-card" style="left:461px">
    <div class="photo" role="img" aria-label="Colleagues meeting around a laptop in a bright office" style="background:linear-gradient(135deg,#e9d9c0,#8a7a66)"></div>
    <div class="date">04<small>OCT</small></div>
    <h4>BUSINESS GROWTH DEPENDS<br>ON YOUR MARKETING</h4>
    <div class="meta">admin &nbsp;/&nbsp; 0 Comments</div>
  </article>

  <div class="abs news-item" style="top:157px"><div class="thumb" role="img" aria-label="Office desk with documents" style="background:linear-gradient(135deg,#d4d7dc,#8d939c)"></div><div><h5>BUSINESS GROWTH DEPENDS ON YOUR MARKETING</h5><div class="meta">admin &nbsp;/&nbsp; 0 Comments</div></div></div>
  <div class="abs news-item" style="top:237px"><div class="thumb" role="img" aria-label="Team meeting at a table" style="background:linear-gradient(135deg,#cfc6b8,#6f665a)"></div><div><h5>BUSINESS GROWTH DEPENDS ON YOUR MARKETING</h5><div class="meta">admin &nbsp;/&nbsp; 0 Comments</div></div></div>
  <div class="abs news-item" style="top:317px"><div class="thumb" role="img" aria-label="Hands pointing at charts" style="background:linear-gradient(135deg,#d9dde2,#939aa4)"></div><div><h5>BUSINESS GROWTH DEPENDS ON YOUR MARKETING</h5><div class="meta">admin &nbsp;/&nbsp; 0 Comments</div></div></div>
  <div class="abs news-item" style="top:395px"><div class="thumb" role="img" aria-label="Workers in a bright office" style="background:linear-gradient(135deg,#e2dcd2,#9b9387)"></div><div><h5>BUSINESS GROWTH DEPENDS ON YOUR MARKETING</h5><div class="meta">admin &nbsp;/&nbsp; 0 Comments</div></div></div>
</section>

<section class="abs cta">
  <h3 class="abs">Accelerate Your Business With KLOMB™!</h3>
  <div class="abs btn">CONTACT NOW!!</div>
</section>

<footer class="abs site-footer">
  <div class="abs contact-row">
    <span>Have any questions?</span>
    <span class="ic"><svg width="12" height="10" viewBox="0 0 12 10" fill="none" stroke="#fff" stroke-width="1.2"><rect x=".6" y=".6" width="10.8" height="8.8"/><path d="M.6 .6 6 5.5 11.4 .6"/></svg></span>
    <span>info@klomb1.example</span>
    <span class="ic" style="margin-left:20px"><svg width="11" height="11" viewBox="0 0 24 24" fill="#fff"><path d="M6.6 10.8a15 15 0 0 0 6.6 6.6l2.2-2.2a1 1 0 0 1 1-.25 11.4 11.4 0 0 0 3.6.57 1 1 0 0 1 1 1V20a1 1 0 0 1-1 1A17 17 0 0 1 3 4a1 1 0 0 1 1-1h3.5a1 1 0 0 1 1 1c0 1.25.2 2.45.57 3.57a1 1 0 0 1-.25 1z"/></svg></span>
    <span>555-010-2722</span>
  </div>
  <div class="abs logo"><span class="dot"></span>KLOMB</div>
  <div class="abs footer-rule"></div>

  <div class="abs about-col">
    <h4>Created By Entrepreneurs For Entrepreneurs</h4>
    <p>Our Story: A team of 7 successful entrepreneurs put their heads together in an effort to help improve the statistics on how many businesses succeed. After tapping into the great minds of business thought leaders from around the globe, they developed the first comprehensive program for small businesses (up to $5M revenues) and packaged it into a simple, affordable, sustainable membership model. And KLOMB™ was born!</p>
  </div>
  <ul class="abs link-col" style="left:493px"><li>About</li><li>Company History</li><li>What We Do</li><li>Testimonials</li><li>Case Studies</li><li>Contact</li></ul>
  <ul class="abs link-col" style="left:625px"><li>Training Programs</li><li>Leadership Team</li><li>Awards &amp; Recognition</li><li>Partners / Clients</li><li>Books</li><li>FAQ</li></ul>
  <div class="abs signup">
    <label>Email address:</label>
    <div class="field">Your email address</div>
    <div class="btn">SIGN UP</div>
  </div>
</footer>

<div class="abs bottom-bar">
  <div class="abs social"><span></span><span></span><span></span></div>
  <div class="abs copyright">Copyright © 2018 KLOMB Systems. All Rights Reserved</div>
</div>

</body>
</html>
```